Tallow Brook Ranch all natural beef packaging

I would like a custom label to affix to my packages of steaks, roasts, and burgers. The packaging label should be simple and represent the all natural, healthy and humane way we raise our grass finished and natural grain finished beef. check out www.tallowbrookranch.example for photos of the ranch and information about our cattle.

Target Market(s)

consumers who wish to purchase beef that is born and raised in Ohio, never given any antibiotics, implants, or hormones. Cattle are never confined, always on pasture, even when finished on grain. Humane treatment of the animals which are handled by horseback and on foot.

Industry/Entity Type

Ranch

Requirements
Must have
• Must be able to incorporate the National Pastureland Society label.
• http://www.nationalpastureland.example/
• I like dark colors, rich and earthy, but maybe on a white background to stand out on the clear plastic wrap over the beef. Imagine you're buying a steak at Parlows and look at how the packaging stands off from the color of the meat.
Nice to have
• I would like a very simple label that incorporates some icon or picture of a calf or cow. See my website www.tallowbrookranch.example

```html
<!DOCTYPE html>
<html lang="en">
<head>
<meta charset="utf-8">
<title>Tallow Brook Ranch – Steak Label</title>
<link href="https://fonts.googleapis.com/css2?family=Lato:wght@400;700&display=swap" rel="stylesheet">
<style>
  :root {
    --page-bg: #ffffff;
    --label-ring: #ffffff;
    --label-ring-edge: #e6e1da;
    --label-field: #9a7b61;
    --badge-green: #1f6a3b;
    --mark-text: #ffffff;
    --tag-cream: #f4ede1;
    --tag-text: #8d6d53;
    --url-text: #ffffff;
  }
  html, body {
    margin: 0;
    padding: 0;
    width: 1200px;
    height: 970px;
    overflow: hidden;
    background: var(--page-bg);
  }
  .canvas {
    position: relative;
    width: 1200px;
    height: 970px;
  }
  .product-label {
    position: absolute;
    left: 0;
    top: 0;
    width: 1200px;
    height: 970px;
  }
  .label-url {
    font-family: "Lato", sans-serif;
    font-weight: 700;
    font-size: 15px;
    fill: var(--url-text);
    letter-spacing: 0.3px;
  }
  .ranch-name {
    font-family: "Lato", sans-serif;
    font-weight: 700;
    font-size: 34px;
    fill: var(--mark-text);
    letter-spacing: 1px;
  }
  .product-name {
    font-family: "Lato", sans-serif;
    font-weight: 400;
    font-size: 36px;
    fill: var(--tag-text);
    letter-spacing: 1px;
  }
  .product-weight {
    font-family: "Lato", sans-serif;
    font-weight: 400;
    font-size: 13px;
    fill: var(--tag-text);
    letter-spacing: 0.5px;
  }
</style>
</head>
<body>
<main class="canvas">
  <svg class="product-label" viewBox="0 0 1200 970" xmlns="http://www.w3.org/2000/svg">
    <ellipse class="label-ring" cx="598" cy="487" rx="308" ry="182"
             fill="var(--label-ring)" stroke="var(--label-ring-edge)" stroke-width="1.5"/>
    <ellipse class="label-field" cx="598" cy="490" rx="281" ry="160" fill="var(--label-field)"/>

    <text class="label-url" x="598" y="364" text-anchor="middle">www.nationalpastureland.example</text>

    <circle class="cert-badge" cx="423" cy="485" r="60" fill="var(--badge-green)"/>

    <g class="ranch-mark">
      <text class="ranch-name" x="600" y="470" text-anchor="middle">TALLOW</text>
      <text class="ranch-name" x="600" y="510" text-anchor="middle">BROOK</text>
      <text class="ranch-name" x="600" y="550" text-anchor="middle">RANCH</text>
    </g>

    <rect class="product-tag" x="474" y="610" width="240" height="72" fill="var(--tag-cream)"/>
    <text class="product-name" x="594" y="648" text-anchor="middle">STEAKS</text>
    <text class="product-weight" x="594" y="670" text-anchor="middle">400G</text>
  </svg>
</main>
</body>
</html>
```